Brand Business Card for Hotel Cloud Management System

Hello designers,
we are looking for a new brand business card for our product Stayvora. Our brand Stayvora is a hotel management system for small hotels, B&B, guesthouses etc. and just recently we are expanding our offer to other European markets. Therefore we need a business card that will communicate not only to the end-users (hoteliers) but also to potential business partners/ We would like the brand business card to be professional looking, but not too serius, modern, elegant, clean, Our brand color is orange, dark grey and it would be nice to see both combined.

Please visit our website www.stayvora.eu to get more impression on what our brand stayvora stands for.

Please find attached stayvora logo.

Target Market(s)

small hotels, hoteliers, B&B owners, potential business partners

Industry/Entity Type

Software Service

Contact Information for Business Card

Stayvora
- hotel software solutions - web booking engine - multi channel manager
www.stayvora.eu
T: +38614738265
E: info@stayvora.net

Font styles to use
Serif
Sans Serif

Colors
f37122
aaaaaa
606060
f6f6f6

Requirements
Must have
• Logo of the brand
• the layout of the business card should be in connection with the look and feel of the website stayvora.eu and logo stayvora;

```html
<!DOCTYPE html>
<html lang="en">
<head>
<meta charset="utf-8">
<title>Stayvora Business Card</title>
<link href="https://fonts.googleapis.com/css2?family=Ubuntu:wght@400;500;700&family=Roboto:wght@400&display=swap" rel="stylesheet">
<style>
  :root {
    --orange: #e2691b;
    --charcoal: #383b3f;
    --ink: #262626;
    --text-grey: #3a3a3a;
    --paper: #f3f3f3;
    --backdrop: #b4b4b4;
    --light: #f0f0f0;
  }
  * { margin: 0; padding: 0; box-sizing: border-box; }
  html, body { width: 1200px; height: 576px; overflow: hidden; }
  body { background: var(--backdrop); position: relative; font-family: "Roboto", Arial, sans-serif; }

  .card {
    position: absolute; top: 139px; width: 484px; height: 291px;
    border-radius: 13px; overflow: hidden;
    box-shadow: 0 2px 5px rgba(0,0,0,.25);
  }
  .card-front { left: 82px; background: var(--charcoal); color: var(--light); }
  .card-back { left: 602px; background: var(--paper); color: var(--text-grey); }

  .brand-name { font-family: "Ubuntu", Arial, sans-serif; font-weight: 500; letter-spacing: -0.5px; line-height: 1; }
  .brand-tagline { font-family: "Ubuntu", Arial, sans-serif; font-weight: 400; line-height: 1; }

  .card-front .brand-name { position: absolute; top: 153px; width: 100%; text-align: center; font-size: 46px; color: var(--light); }
  .card-front .brand-tagline { position: absolute; top: 200px; width: 100%; text-align: center; font-size: 14px; color: #d8d8d8; }

  .services { position: absolute; top: 263px; width: 100%; text-align: center; font-size: 12px; color: #e6e6e6; }
  .services .sep { color: var(--orange); margin: 0 5px; }

  .card-back .brand-name { position: absolute; left: 26px; top: 64px; font-size: 40px; color: var(--ink); }
  .card-back .brand-tagline { position: absolute; left: 26px; top: 103px; font-size: 13px; color: var(--ink); }

  .accent-band { position: absolute; right: 0; top: 0; width: 14px; height: 100%; background: var(--orange); }

  .person-name { position: absolute; left: 26px; top: 153px; font-family: "Ubuntu", Arial, sans-serif; font-weight: 500; font-size: 18px; color: var(--orange); }
  .person-title { position: absolute; left: 26px; top: 177px; font-size: 13px; color: var(--text-grey); }

  .contact-list { position: absolute; left: 26px; top: 210px; list-style: none; }
  .contact-list li { display: flex; align-items: center; height: 18px; font-size: 13px; color: var(--ink); }
  .contact-list svg { width: 11px; height: 11px; margin-right: 13px; fill: var(--orange); }
</style>
</head>
<body>

<section class="card card-front">
  <div class="brand-name">Stayvora</div>
  <div class="brand-tagline">hotel pms service</div>
  <div class="services">Hotel Software Solutions<span class="sep">|</span>Web Booking Engine<span class="sep">|</span>Multi Channel Manager</div>
</section>

<section class="card card-back">
  <div class="brand-name">Stayvora</div>
  <div class="brand-tagline">hotel pms service</div>
  <div class="accent-band"></div>

  <div class="person-name">Marko Velin</div>
  <div class="person-title">Managing Director</div>

  <ul class="contact-list">
    <li>
      <svg viewBox="0 0 12 12" aria-hidden="true"><path d="M1 4c0-1.5 2-2.5 5-2.5S11 2.5 11 4v1H8.5V4h-5v1H1z"/><path d="M3 6h6l1.5 4.5h-9z"/></svg>
      +38614738265
    </li>
    <li>
      <svg viewBox="0 0 12 12" aria-hidden="true"><path d="M0.5 2.5h11v7h-11z M1.5 3.3 6 6.8l4.5-3.5" /><path d="M0.5 2.5 6 7l5.5-4.5v7h-11z"/></svg>
      info@stayvora.net
    </li>
    <li>
      <svg viewBox="0 0 12 12" aria-hidden="true"><circle cx="6" cy="6" r="5.5"/><path d="M0.5 6h11M6 .5c-2.5 3-2.5 8 0 11M6 .5c2.5 3 2.5 8 0 11" stroke="#f3f3f3" stroke-width="0.9" fill="none"/></svg>
      www.stayvora.eu
    </li>
  </ul>
</section>

</body>
</html>
```